Tech Savy small Business accountant business card design

We need a business card for a new company based in the cloud. We provide tax, business advisory, accounting, information technology solutions and back office functions to small businesses. We offer fixed fee packages with add on services as you need them. By harnessing technology we simplify small business operational processes providing valuable time and information for small business owners to grow their business. In the logo (zulvarine) we want to be able to see zulv and experts. The final design should communicate achieving growth dreams and balance (ie life and $).
Updates
This project has been temporarily placed on hold until I finalize "Tech Savy small Business accountant needs a logo". I invite all designers to submit on this logo project. Once my logo is finalized I will resume this business card contest. Thanks Added Wednesday, March 19, 2014
This project has been temporarily placed on hold until I finalize "Tech Savy small Business accountant logo". I invite all designers to submit on this logo project. Once my logo is finalized I will resume this business card contest. Thanks Added Thursday, March 20, 2014
Target Market(s)
Small Business (Revenue $500,000, more than 3 employees) owners.
Industry/Entity Type
Small Business
Contact Information for Business Card
Marla Pennick (Principal)
Accountant, Tax Agent.
TEL | 0417 583 916
EMAIL | Marla.Pennick@zulvarine.com.au
WEB | www.zulvarine.com.au
Look and feel

```html
<!DOCTYPE html>
<html lang="en">
<head>
<meta charset="utf-8">
<title>zulvarine business card</title>
<link rel="stylesheet" href="https://fonts.googleapis.com/css2?family=Open+Sans:wght@400;600;700&display=swap">
<style>
  :root {
    --brand-blue: #1a9ad6;
    --brand-grey: #6d6e71;
    --text-grey: #555658;
    --card-white: #ffffff;
    --page-bg: #e9e7e4;
  }
  * { box-sizing: border-box; margin: 0; padding: 0; }
  html, body {
    width: 1200px; height: 1000px; overflow: hidden;
    background: var(--page-bg);
    font-family: "Open Sans", Arial, sans-serif;
  }
  .canvas { position: relative; width: 1200px; height: 1000px; }

  .card {
    position: absolute; left: 265px; width: 666px; height: 397px;
    border-radius: 22px; overflow: hidden;
    box-shadow: 0 3px 10px rgba(0,0,0,0.25);
  }
  .card--front { top: 73px; background: var(--card-white); }
  .card--back { top: 533px; background: var(--brand-blue); }

  /* front: brand block */
  .brand { position: absolute; left: 38px; top: 152px; }
  .brand__name {
    font-weight: 700; font-size: 50px; line-height: 1;
    color: var(--brand-blue); letter-spacing: -1px;
  }
  .brand__tagline {
    margin-top: 6px; font-size: 14.5px; color: var(--text-grey);
  }

  /* front: person and contact */
  .person { position: absolute; left: 368px; top: 114px; color: var(--text-grey); }
  .person__name { font-weight: 700; font-size: 21px; color: var(--brand-blue); }
  .person__role { font-size: 15.5px; line-height: 24px; }
  .person__role-first { font-size: 15.5px; }

  .contact { position: absolute; left: 368px; top: 200px; list-style: none; }
  .contact__item {
    display: flex; align-items: center; gap: 6px;
    height: 24px; font-size: 15px; color: var(--text-grey);
  }
  .contact__icon { width: 15px; height: 15px; fill: var(--brand-blue); flex: none; }
  .contact__strong { font-weight: 700; color: var(--brand-blue); }

  /* front: footer bands */
  .band { position: absolute; top: 339px; height: 38px; }
  .band--blue { left: 0; width: 520px; background: var(--brand-blue); }
  .band--grey { left: 566px; right: 0; background: var(--brand-grey); }

  /* back */
  .back-brand {
    position: absolute; left: 0; right: 0; top: 140px; text-align: center; color: var(--card-white);
  }
  .back-brand__name { font-weight: 700; font-size: 72px; line-height: 1; letter-spacing: -1.5px; }
  .back-brand__tagline { margin-top: 14px; font-size: 21px; }
</style>
</head>
<body>
<main class="canvas">

  <section class="card card--front" aria-label="Business card front">
    <div class="brand">
      <div class="brand__name">zulvarine</div>
      <div class="brand__tagline">Your business and accounting partner</div>
    </div>

    <div class="person">
      <p><span class="person__name">Marla Pennick</span> <span class="person__role-first">/ Principal</span></p>
      <p class="person__role">Accountant, Tax Agent</p>
    </div>

    <ul class="contact">
      <li class="contact__item">
        <svg class="contact__icon" viewBox="0 0 16 16" aria-hidden="true">
          <path d="M2 6c0-2 2.5-3 6-3s6 1 6 3v1h-3V5.5C10 5 9 5 8 5S6 5 5 5.5V7H2z"/>
          <path d="M4 8h8l1.5 5h-11z"/>
        </svg>
        <span>0417 583 916</span>
      </li>
      <li class="contact__item">
        <svg class="contact__icon" viewBox="0 0 16 16" aria-hidden="true">
          <path d="M1 4h14v9H1z"/>
          <path d="M1 4l7 5 7-5" fill="none" stroke="#fff" stroke-width="1.3"/>
        </svg>
        <span>Marla.Pennick@zulvarine.com.au</span>
      </li>
      <li class="contact__item">
        <svg class="contact__icon" viewBox="0 0 16 16" aria-hidden="true">
          <circle cx="8" cy="8" r="6.5" fill="none" stroke="var(--brand-blue)" stroke-width="1.3"/>
          <ellipse cx="8" cy="8" rx="2.7" ry="6.5" fill="none" stroke="var(--brand-blue)" stroke-width="1.1"/>
          <path d="M1.5 8h13M2.5 5h11M2.5 11h11" stroke="var(--brand-blue)" stroke-width="1"/>
        </svg>
        <span>www.<span class="contact__strong">zulvarine</span>.com.au</span>
      </li>
    </ul>

    <div class="band band--blue"></div>
    <div class="band band--grey"></div>
  </section>

  <section class="card card--back" aria-label="Business card back">
    <div class="back-brand">
      <div class="back-brand__name">zulvarine</div>
      <div class="back-brand__tagline">Your business and accounting partner</div>
    </div>
  </section>

</main>
</body>
</html>
```